New business logo / Business Card Design

My company provides Interim Management and consultancy, for Facilities Services. Covers any aspect of facilities management, including M&E, helpdesk, asset management, supplier relationships, catering, cleaning etc. Company provides innovative solutions to exceed client needs, drawing on years of experience. Initial thoughts on logo are attached below. Fits with RAG status on projects, red, amber and green, with logo design colours around moving services from amber to green.

Target Market(s)

Facilities Management clients and service providers

Industry/Entity Type

Business

Contact Information for Business Card

Company Name = k7Rventures Ltd My name on card = Derek Hallam, Director Mobile = 07719360458 Email = Derek@k7rventuresltd.example.co.uk Twitter = @k7Rventures Ltd

Font styles to use
Sans Serif

Colors
f37122
00a990

Requirements
Must have
• Logo to be evident, with some background image in reference to Facilities Management

```html
<!DOCTYPE html>
<html lang="en">
<head>
<meta charset="utf-8">
<title>k7Rventures Ltd — Business Card</title>
<link rel="stylesheet" href="https://fonts.googleapis.com/css2?family=Source+Sans+3:ital,wght@0,400;0,600;0,700;1,400&display=swap">
<style>
  :root {
    --backdrop: #9c9e9d;
    --card-light: #ecedef;
    --card-dark: #060606;
    --orange: #d9560e;
    --green: #1a6d12;
    --ink: #2d2d2d;
    --pattern-dark: #151515;
    --white: #f4f4f4;
  }
  * { margin: 0; padding: 0; box-sizing: border-box; }
  html, body {
    width: 1105px; height: 1200px; overflow: hidden;
    background: var(--backdrop);
    font-family: "Source Sans 3", Arial, sans-serif;
  }
  .stage { position: relative; width: 1105px; height: 1200px; }

  .card {
    position: absolute; left: 180px; width: 746px; height: 426px;
    overflow: hidden;
  }
  .card--front { top: 119px; background: var(--card-light); }
  .card--back { top: 637px; background: var(--card-dark); }

  .company-name {
    position: absolute; left: 63px; top: 190px;
    font-size: 30px; font-weight: 700; color: var(--ink);
    letter-spacing: 0.2px;
  }

  .person { position: absolute; left: 378px; top: 90px; }
  .person__name { font-size: 28px; font-weight: 600; color: var(--orange); line-height: 1.1; }
  .person__role { font-size: 19px; font-weight: 400; color: var(--green); margin-top: 2px; }

  .contact-list { position: absolute; left: 388px; top: 170px; list-style: none; }
  .contact-list li {
    display: flex; align-items: center; height: 34.5px;
    font-size: 19px; color: var(--ink);
  }
  .contact-list svg { width: 18px; height: 18px; margin-right: 12px; flex: none; }

  .colour-band { position: absolute; left: 0; bottom: 0; width: 746px; height: 26px; }

  .back-pattern {
    position: absolute; inset: 0;
    background: linear-gradient(180deg, var(--pattern-dark), #0b0b0b 60%, var(--pattern-dark));
  }
  .back-logo {
    position: absolute; left: 0; right: 0; top: 170px;
    text-align: center; font-size: 96px; font-weight: 700;
    color: var(--white); line-height: 1;
  }
  .services {
    position: absolute; left: 0; right: 0; top: 320px;
    text-align: center; font-style: italic; font-size: 18.5px;
    line-height: 29px; color: var(--white);
  }
</style>
</head>
<body>
<main class="stage">

  <section class="card card--front" aria-label="Business card front">
    <div class="company-name">k7Rventures Ltd</div>

    <div class="person">
      <div class="person__name">Derek Hallam</div>
      <div class="person__role">Director</div>
    </div>

    <ul class="contact-list">
      <li>
        <svg viewBox="0 0 18 18" aria-hidden="true"><rect x="4" y="1" width="10" height="16" rx="2" fill="none" stroke="var(--orange)" stroke-width="2"/><rect x="7.5" y="13.5" width="3" height="1.5" fill="var(--orange)"/></svg>
        07719360458
      </li>
      <li>
        <svg viewBox="0 0 18 18" aria-hidden="true"><circle cx="9" cy="9" r="7" fill="var(--orange)"/></svg>
        @k7Rventures Ltd
      </li>
      <li>
        <svg viewBox="0 0 18 18" aria-hidden="true"><rect x="1" y="3.5" width="16" height="11" fill="var(--orange)"/><path d="M1.5 4 9 10 16.5 4" fill="none" stroke="var(--card-light)" stroke-width="1.4"/></svg>
        Derek@k7rventuresltd.example.co.uk
      </li>
      <li>
        <svg viewBox="0 0 18 18" aria-hidden="true"><circle cx="9" cy="9" r="7.5" fill="var(--orange)"/><path d="M5 6c2 0 3 1 2.5 3S9 12 8 15M11 3c0 2 1 3 3 3.5M12 10c1 1 1 3 0 4" fill="none" stroke="var(--card-light)" stroke-width="1.3"/></svg>
        www.k7rventuresltd.example.co.uk
      </li>
    </ul>

    <svg class="colour-band" viewBox="0 0 746 26" preserveAspectRatio="none" aria-hidden="true">
      <polygon points="0,0 261,0 244,26 0,26" fill="var(--orange)"/>
      <polygon points="267,0 507,0 490,26 250,26" fill="var(--card-dark)"/>
      <polygon points="513,0 746,0 746,26 496,26" fill="var(--green)"/>
    </svg>
  </section>

  <section class="card card--back" aria-label="Business card back">
    <div class="back-pattern" role="img" aria-label="Faint repeating tagline pattern across the dark background"></div>
    <div class="back-logo">k7R</div>
    <p class="services">
      Facilities management, including M&amp;E, helpdesk<br>
      asset management, supplier relationships, catering, cleaning etc.
    </p>
  </section>

</main>
</body>
</html>
```